Meadowrun Honey labels

I have honey farm . I would like to sale it at grocery stores. I need really unique and very attractive designed labels, I would like to see writings 100% Natural honey and GMO free ,. Company name "MeadowrunHoney" . I want to put 2 labels and one ribbon tag in middle and round label on top of lid(only one diamond shape in the middle).I would like to see bee flying over red flower and at the left side flower field and right side bee putting honey into honey hives. I have attached example pictures of Honey Jars labels, tags and type. I have two different type of Honey jars i have also attached picture of those jars. For jar with red lid. If middle label little bit bigger than measurement thats ok because writing has to fit.

Target Market(s)

Grocery stores

Industry/Entity Type

Farm

Requirements
Must have
• 100% Natural Honey, GMO Free, Company name Meadowrun Honey, attractive and unique design. bee flying over flower, right side label flower field left side bee putting honey into bee hives.

```html
<!DOCTYPE html>
<html lang="en">
<head>
<meta charset="utf-8">
<title>Meadowrun Honey — Jar Ribbon Labels</title>
<link rel="stylesheet" href="https://fonts.googleapis.com/css2?family=Open+Sans:wght@400;600;700&display=swap">
<style>
  :root {
    --paper: #ffffff;
    --band-amber: #856537;
    --band-amber-soft: #93734a;
    --band-sage: #c6c393;
    --band-sage-soft: #d1cea4;
    --label-cream: #f6e38f;
    --ink-brown: #7a5a35;
    --accent-orange: #e8702a;
    --art-orange: #ee8a3c;
  }
  html, body {
    margin: 0;
    padding: 0;
    width: 1200px;
    height: 915px;
    overflow: hidden;
    background: var(--paper);
  }
  .sheet { display: block; width: 1200px; height: 915px; }
  .band--amber { fill: var(--band-amber); }
  .band--sage { fill: var(--band-sage); }
  .pattern-area--amber { fill: url(#amberComb); }
  .pattern-area--sage { fill: url(#sageComb); }
  .hex-label { fill: var(--label-cream); }
  .brand-name {
    font-family: "Open Sans", sans-serif;
    font-weight: 700;
    fill: var(--ink-brown);
    text-anchor: middle;
  }
  .brand-name--small { font-size: 17px; letter-spacing: 4px; }
  .brand-name--large { font-size: 60px; letter-spacing: -1px; }
  .ornament-area { fill: var(--art-orange); opacity: 0.35; }
  .claim {
    font-family: "Open Sans", sans-serif;
    fill: var(--accent-orange);
    text-anchor: middle;
  }
  .claim--percent { font-size: 16px; font-weight: 600; }
  .claim--natural { font-size: 12.5px; font-weight: 400; letter-spacing: 1.5px; }
  .claim-gmo {
    font-family: "Open Sans", sans-serif;
    fill: var(--ink-brown);
    font-size: 10.5px;
    font-weight: 400;
    text-anchor: middle;
  }
</style>
</head>
<body>
<svg class="sheet" viewBox="0 0 1200 915" xmlns="http://www.w3.org/2000/svg">
  <defs>
    <linearGradient id="amberComb" x1="0" y1="0" x2="0" y2="1">
      <stop offset="0" stop-color="var(--band-amber)"/>
      <stop offset="0.5" stop-color="var(--band-amber-soft)"/>
      <stop offset="1" stop-color="var(--band-amber)"/>
    </linearGradient>
    <linearGradient id="sageComb" x1="0" y1="0" x2="0" y2="1">
      <stop offset="0" stop-color="var(--band-sage)"/>
      <stop offset="0.5" stop-color="var(--band-sage-soft)"/>
      <stop offset="1" stop-color="var(--band-sage)"/>
    </linearGradient>
  </defs>

  <g class="label-set label-set--amber">
    <rect class="band band--amber" x="10" y="212" width="1175" height="128"/>
    <rect class="pattern-area pattern-area--amber" x="18" y="228" width="1160" height="96" role="img" aria-label="Faint honeycomb hexagon pattern across the band"/>
    <polygon class="hex-label" points="596,145 704,188 704,364 596,407 489,364 489,188"/>
    <text class="brand-name brand-name--small" x="596" y="188">MEADOWRUN</text>
    <text class="brand-name brand-name--large" x="596" y="258">Honey</text>
    <rect class="ornament-area" x="512" y="272" width="172" height="84" rx="8" role="img" aria-label="Beehive skep with flying bees, curling vines and a ribbon banner"/>
    <text class="claim claim--percent" x="598" y="352">100%</text>
    <text class="claim claim--natural" x="598" y="369">NATURAL HONEY</text>
    <text class="claim-gmo" x="598" y="385">GMO FREE</text>
  </g>

  <g class="label-set label-set--sage">
    <rect class="band band--sage" x="10" y="514" width="1175" height="128"/>
    <rect class="pattern-area pattern-area--sage" x="18" y="530" width="1160" height="96" role="img" aria-label="Faint honeycomb hexagon pattern across the band"/>
    <polygon class="hex-label" points="595,447 703,490 703,666 595,709 487,666 487,490"/>
    <text class="brand-name brand-name--small" x="595" y="490">MEADOWRUN</text>
    <text class="brand-name brand-name--large" x="595" y="560">Honey</text>
    <rect class="ornament-area" x="540" y="576" width="116" height="58" rx="8" role="img" aria-label="Beehive skep with flying bees and curling vines"/>
    <text class="claim claim--percent" x="597" y="653">100%</text>
    <text class="claim claim--natural" x="597" y="667">NATURAL HONEY</text>
    <text class="claim-gmo" x="597" y="688">GMO Free</text>
  </g>
</svg>
</body>
</html>
```